Business Card Design - Furniture Retail

Open to both Single or double sided design

We are launching a online ecommerce store that sells Scandinavian/Danish style of furniture in Australia.

We aspire to provide stylish but classic and designers' selection of furniture to the Australia public at affordable price. For the style of the furniture we are selling, please see the following links:

https://www.filecrate.example/sh/qk3mzr8wlp/BXTpLnR4vQ7cYdHs?dl=0

The style of the design we are looking for is clean, simple that look Scandinavian/Danish but yet it is timeless classic.

Aspiring Design
http://www.lindmora.com
http://tobyquell.com.au/
http://vekt.furniture/
http://www.olvo.com/
Updates

Please display the card on normal angle for both front and back instead of funny angle. Please keep it display when displaying the design of the business cards so that we can focus on the designs rather than being confused by the unnecessary stuffs like the hands or background

I think there is already enough curve line on the logo itself so anything extra of the curve on the business card would be really unnecessary. Please avoid using any of the extra curve line on the business card, other than the logo itself. Thanks

Regular card and give them a matt celloglaze to create texture on card that makes it looked luxury and expensive.

Please display design on normal angle! Please only use white colour in the background (not the business card but the referring to the submission) rather than anything fancy so that we can focus on the design.

Target Market(s)

High end market consumers who are financially capable and who has good taste and appreciate good design

aged between 28 - 45 white collars professional/businessmen who live in metropolitan areas

Industry/Entity Type

Business

Font styles to use
Serif
Sans Serif

Requirements
Must have
• Regular card and give them a matt celloglaze to create texture on card that makes it looked luxury and expensive.

Please use the logo from the uploaded files

Company Name: Milo Verhagen
Name: Milo Reeb
Phone: +614 27 305 641
Website: www.miloverhagen.com.au
Email: milo@miloverhagen.com.au
Nice to have
• Colour is not limited to black and white
Should not have
• The concept photos of the furniture should NOT be used in the FRONT page of the business card.

```html
<!DOCTYPE html>
<html lang="en">
<head>
<meta charset="utf-8">
<title>Milo Verhagen – Business Card</title>
<link href="https://fonts.googleapis.com/css2?family=Open+Sans:wght@400;700&family=Cinzel:wght@400&display=swap" rel="stylesheet">
<style>
  :root {
    --page: #ffffff;
    --card: #fbfbfb;
    --ink: #1a1a1a;
    --text: #333333;
    --band: #141414;
    --band-grey: #8c8c8c;
    --accent-grey: #8f8782;
    --rule: #2b2b2b;
  }
  * { margin: 0; padding: 0; box-sizing: border-box; }
  html, body {
    width: 1200px; height: 675px; overflow: hidden;
    background: var(--page);
    font-family: "Open Sans", Arial, sans-serif;
  }
  .stage {
    width: 1200px; height: 675px;
    display: flex; align-items: center; justify-content: center; gap: 60px;
  }
  .card {
    position: relative;
    width: 525px; height: 300px;
    background: var(--card);
    box-shadow: 0 0 0 1px #e2e2e2, 0 6px 18px rgba(0,0,0,0.10);
    overflow: hidden;
  }

  /* front */
  .front-band { position: absolute; left: 0; bottom: 0; width: 100%; height: 80px; }
  .front-name {
    position: absolute; right: 34px; top: 30px;
    font-weight: 700; font-size: 19px; letter-spacing: 0.5px; color: var(--ink);
  }
  .contact-list {
    position: absolute; right: 34px; top: 82px;
    list-style: none; text-align: right;
    font-size: 11.5px; line-height: 19px; color: var(--text);
  }
  .contact-list li { display: flex; justify-content: flex-end; align-items: center; gap: 8px; }
  .contact-list svg { width: 11px; height: 11px; fill: var(--ink); }
  .divider-rule {
    position: absolute; left: 195px; top: 130px; width: 140px; height: 1.2px;
    background: var(--rule); transform: rotate(-22deg); transform-origin: left center;
  }
  .wordmark {
    font-family: "Cinzel", Georgia, serif;
    font-weight: 400; color: var(--ink); letter-spacing: 1px;
  }
  .front .wordmark { position: absolute; left: 30px; top: 150px; font-size: 25px; }

  /* back */
  .url-bar {
    position: absolute; left: 48px; top: 0; width: 34px; height: 228px;
    background: var(--band);
    display: flex; align-items: center; justify-content: center;
  }
  .url-bar span {
    writing-mode: vertical-rl;
    color: #ffffff; font-size: 12.5px; letter-spacing: 0.8px;
  }
  .url-square {
    position: absolute; left: 48px; top: 238px; width: 34px; height: 14px;
    background: var(--accent-grey);
  }
  .back .wordmark {
    position: absolute; left: 130px; right: 20px; top: 128px;
    text-align: center; font-size: 30px;
  }
</style>
</head>
<body>
<main class="stage">

  <section class="card front" aria-label="Card front">
    <h1 class="front-name">MILO VERHAGEN</h1>
    <ul class="contact-list">
      <li>MILO REEB
        <svg viewBox="0 0 12 12"><circle cx="6" cy="3.5" r="2.8"/><path d="M0.5 12 C1 7.5 11 7.5 11.5 12 Z"/></svg></li>
      <li>+614 27 305 641
        <svg viewBox="0 0 12 12"><rect x="0.5" y="3" width="11" height="8.5" rx="1"/><rect x="3" y="0.5" width="6" height="3" rx="1"/></svg></li>
      <li>MILO@MILOVERHAGEN.COM.AU
        <svg viewBox="0 0 12 12"><path d="M0.5 2 H11.5 V10.5 H0.5 Z M1.5 3 L6 6.8 L10.5 3 Z" fill-rule="evenodd"/></svg></li>
      <li>WWW.MILOVERHAGEN.COM.AU
        <svg viewBox="0 0 12 12"><path d="M0.5 1 H11.5 V8.5 H0.5 Z M1.8 2.2 V7.3 H10.2 V2.2 Z M4 10 H8 V11.5 H4 Z" fill-rule="evenodd"/></svg></li>
    </ul>
    <div class="divider-rule"></div>
    <p class="wordmark">MILO VERHAGEN</p>
    <svg class="front-band" viewBox="0 0 525 80" preserveAspectRatio="none" aria-hidden="true">
      <path d="M0 50 H270 L285 28 H525 V80 H0 Z" fill="var(--band-grey)"/>
      <path d="M0 60 H274 L289 38 H525 V80 H0 Z" fill="var(--band)"/>
    </svg>
  </section>

  <section class="card back" aria-label="Card back">
    <div class="url-bar"><span>WWW.MILOVERHAGEN.COM.AU</span></div>
    <div class="url-square"></div>
    <p class="wordmark">MILO VERHAGEN</p>
  </section>

</main>
</body>
</html>
```